Stationary Design for Stunning new Logo

I need to envelopes, letterhead, business cards designed to compliment our new logo.

We are a 25 year old printing company going through a brand refresh. All items should have the design extended to both sides for full print ability.

Industry/Entity Type

Printing

Requirements
Must have
• It must utilize the new logo & colors PMS 300 & PMS 295.

```html
<!DOCTYPE html>
<html lang="en">
<head>
<meta charset="utf-8">
<title>Northmark Stationery Set</title>
<link rel="stylesheet" href="https://fonts.googleapis.com/css2?family=Open+Sans:wght@400;600;700&display=swap">
<style>
  :root {
    --pms-300: #005eb8;
    --pms-295: #002855;
    --paper: #ffffff;
    --backdrop: #e6e8ec;
    --ink: #4a4f57;
    --ink-soft: #8a9099;
    --flap: #f3f4f6;
    --flap-edge: #d6d9de;
  }
  * { box-sizing: border-box; margin: 0; padding: 0; }
  html, body { width: 1200px; height: 816px; overflow: hidden; }
  body {
    background: var(--backdrop);
    font-family: "Open Sans", Arial, sans-serif;
    color: var(--ink);
    position: relative;
  }
  .sheet {
    position: absolute;
    background: var(--paper);
    box-shadow: 0 6px 18px rgba(0, 30, 70, 0.16);
    overflow: hidden;
  }

  /* Footer bands: a solid PMS 300 strip with a thin PMS 295 rule above it */
  .footer-band {
    position: absolute;
    left: 0; right: 0; bottom: 0;
    height: var(--band-h, 12px);
    background: var(--pms-300);
  }
  .footer-rule {
    position: absolute;
    left: 0; right: 0;
    bottom: calc(var(--band-h, 12px) + var(--rule-gap, 5px));
    height: var(--rule-h, 3px);
    background: var(--pms-295);
  }

  .brand { display: flex; align-items: center; gap: 6px; white-space: nowrap; }
  .brand-dot {
    border-radius: 50%;
    background: var(--pms-300);
    flex: none;
  }
  .brand-name {
    font-weight: 700;
    color: var(--pms-295);
    letter-spacing: 0.04em;
    line-height: 1;
  }
  .brand-tagline {
    color: var(--pms-300);
    text-transform: uppercase;
    letter-spacing: 0.12em;
    line-height: 1;
    margin-top: 3px;
  }

  /* Letterhead */
  .letterhead { left: 230px; top: 40px; width: 330px; height: 467px; }
  .letterhead .brand { position: absolute; left: 26px; top: 24px; }
  .letterhead .brand-dot { width: 16px; height: 16px; }
  .letterhead .brand-name { font-size: 15px; }
  .letterhead .brand-tagline { font-size: 5px; }
  .letter-body {
    position: absolute;
    left: 26px; top: 72px; right: 30px;
    font-size: 6.4px;
    line-height: 1.45;
  }
  .letter-body p { margin-bottom: 7px; }

  /* Cover sheet */
  .cover { left: 600px; top: 40px; width: 330px; height: 467px; }
  .cover .brand { position: absolute; left: 50%; top: 150px; transform: translateX(-50%); gap: 10px; }
  .cover .brand-dot { width: 30px; height: 30px; }
  .cover .brand-name { font-size: 30px; }
  .cover .brand-tagline { font-size: 8px; margin-top: 5px; }

  .letterhead, .cover { --band-h: 14px; --rule-gap: 6px; --rule-h: 3px; }

  /* Business cards */
  .card { left: 30px; width: 180px; height: 103px; --band-h: 6px; --rule-gap: 3px; --rule-h: 2px; }
  .card-front { top: 230px; }
  .card-front .brand { position: absolute; left: 16px; top: 30px; }
  .card-front .brand-dot { width: 13px; height: 13px; }
  .card-front .brand-name { font-size: 13px; }
  .card-front .brand-tagline { font-size: 4.5px; }
  .card-back { top: 355px; }
  .card-back .brand-dot { position: absolute; right: 16px; top: 14px; width: 18px; height: 18px; }
  .contact {
    position: absolute; left: 14px; top: 24px;
    font-size: 6px; line-height: 1.4;
  }
  .contact .person { font-size: 8px; font-weight: 600; color: var(--pms-295); }
  .contact .role { color: var(--ink-soft); margin-bottom: 4px; }

  /* Envelopes */
  .envelope { top: 550px; width: 420px; height: 210px; --band-h: 10px; --rule-gap: 5px; --rule-h: 3px; }
  .envelope-front { left: 230px; }
  .envelope-front .brand { position: absolute; right: 26px; top: 22px; }
  .envelope-front .brand-dot { width: 12px; height: 12px; }
  .envelope-front .brand-name { font-size: 12px; }
  .envelope-front .brand-tagline { font-size: 4.5px; }
  .envelope-back { left: 690px; }
  .envelope-flap { position: absolute; left: 0; top: 0; width: 100%; height: 70px; display: block; }
  .envelope-flap path { fill: var(--flap); stroke: var(--flap-edge); stroke-width: 1; }
  .envelope-back .brand-dot { position: absolute; left: 50%; top: 22px; width: 18px; height: 18px; transform: translateX(-50%); }
</style>
</head>
<body>

  <section class="sheet letterhead">
    <div class="brand">
      <span class="brand-dot"></span>
      <div>
        <div class="brand-name">NORTHMARK</div>
        <div class="brand-tagline">Commercial Printing</div>
      </div>
    </div>
    <div class="letter-body">
      <p>2480 Harbor Crest Lane<br>Fairview, OR 97024</p>
      <p>March 14th, 2012</p>
      <p>Ms. Dalton<br>Director, Alder Youth Center<br>118 Westfield Road<br>Brookline, NH 03033</p>
      <p>Dear Ms. Dalton:</p>
      <p>In the first paragraph, the writer gives a brief introduction and states the reason for the letter. The second paragraph holds the details and plays the main role in the letter. Keep sentences short and to the point.</p>
      <p>The third and last paragraph closes the letter and can be kept short.</p>
      <p>Sincerely,</p>
      <p>(Signature of the writer goes here)</p>
      <p>Marcus Hale</p>
    </div>
    <span class="footer-rule"></span>
    <span class="footer-band"></span>
  </section>

  <section class="sheet cover">
    <div class="brand">
      <span class="brand-dot"></span>
      <div>
        <div class="brand-name">NORTHMARK</div>
        <div class="brand-tagline">Commercial Printing</div>
      </div>
    </div>
    <span class="footer-rule"></span>
    <span class="footer-band"></span>
  </section>

  <section class="sheet card card-front">
    <div class="brand">
      <span class="brand-dot"></span>
      <div>
        <div class="brand-name">NORTHMARK</div>
        <div class="brand-tagline">Commercial Printing</div>
      </div>
    </div>
    <span class="footer-rule"></span>
    <span class="footer-band"></span>
  </section>

  <section class="sheet card card-back">
    <span class="brand-dot"></span>
    <div class="contact">
      <div class="person">Your Name</div>
      <div class="role">Position</div>
      <div>Phone: 555 0142 2210</div>
      <div>Mobile: 555 0188 4407</div>
      <div>Email: name@northmark.com</div>
    </div>
    <span class="footer-rule"></span>
    <span class="footer-band"></span>
  </section>

  <section class="sheet envelope envelope-front">
    <div class="brand">
      <span class="brand-dot"></span>
      <div>
        <div class="brand-name">NORTHMARK</div>
        <div class="brand-tagline">Commercial Printing</div>
      </div>
    </div>
    <span class="footer-rule"></span>
    <span class="footer-band"></span>
  </section>

  <section class="sheet envelope envelope-back">
    <svg class="envelope-flap" viewBox="0 0 420 70" preserveAspectRatio="none" aria-hidden="true">
      <path d="M0 0 L420 0 L420 8 L250 66 Q210 74 170 66 L0 8 Z"/>
    </svg>
    <span class="brand-dot"></span>
    <span class="footer-rule"></span>
    <span class="footer-band"></span>
  </section>

</body>
</html>
```